willowcreekrestoring - healing business promotion

I have and energy / intuitive healing and kinesiology business. working with people who are looking for healing outside of the modern medical model, who have tried but failed in their search for understanding their conditions and why health and or happiness eludes them. the healing is done with love, patience and understanding. I am looking to be taken seriously with my presentation and to reach a person who may be deterred by the thought of angels and intuition! but to not exclude those that are attracted to that also.

Industry/Entity Type

Medical

Contact Information for Business Card

willowcreekrestoring
fast safe deep energy healing system
tamsin louise harte
energy healing / kinesiology and neurotraining
0417266183 07 4158 2746
home visits available for cairns and tablelands
t.lharte@quillmail.com

Requirements
Should not have
• Primary colours

```html
<!DOCTYPE html>
<html lang="en">
<head>
<meta charset="utf-8">
<title>Willow Creek Restoring – Business Card</title>
<link rel="stylesheet" href="https://fonts.googleapis.com/css2?family=Almendra+SC&family=Arimo:wght@400;700&display=swap">
<style>
  :root {
    --navy-deep: #1b3466;
    --navy-mid: #2a4a82;
    --navy-light: #34568f;
    --ink-blue: #1f3d78;
    --text-blue: #2b3f8c;
    --white: #ffffff;
    --rule-light: #e6e8ec;
    --rule-dark: #9aa0a8;
    --frame: #222222;
    --page: #ffffff;
  }
  * { box-sizing: border-box; margin: 0; padding: 0; }
  html, body { width: 1200px; height: 399px; overflow: hidden; background: var(--page); }
  .canvas { position: relative; width: 1200px; height: 399px; }

  .card {
    position: absolute;
    top: 26px;
    width: 530px;
    height: 311px;
    border: 1px solid var(--frame);
    background: var(--white);
    overflow: hidden;
  }
  .card--front { left: 30px; }
  .card--back { left: 621px; }

  .card__band {
    position: absolute;
    left: 0; top: 0;
    width: 100%;
    height: 152px;
    background:
      radial-gradient(ellipse at 30% 40%, rgba(255,255,255,0.05), transparent 60%),
      linear-gradient(180deg, var(--navy-deep) 0%, var(--navy-mid) 55%, var(--navy-light) 100%);
  }
  .card__rule {
    position: absolute;
    left: 0; top: 152px;
    width: 100%;
    height: 13px;
    background: linear-gradient(180deg, var(--rule-dark) 0%, var(--rule-light) 45%, var(--white) 60%, var(--rule-dark) 100%);
  }

  .brand-name {
    font-family: "Almendra SC", serif;
    font-size: 31px;
    letter-spacing: 0.5px;
    white-space: nowrap;
    text-align: center;
    position: absolute;
    left: 0; width: 100%;
  }
  .card--front .brand-name { top: 61px; color: var(--white); }
  .card--back .brand-name { top: 215px; color: var(--ink-blue); }

  .tagline {
    position: absolute;
    left: 0; width: 100%;
    top: 84px;
    text-align: center;
    font-family: "Arimo", Arial, sans-serif;
    font-size: 17.5px;
    line-height: 22px;
    color: var(--white);
  }

  .contact-list {
    position: absolute;
    left: 238px;
    top: 174px;
    list-style: none;
  }
  .contact-list li {
    display: flex;
    align-items: center;
    gap: 6px;
    height: 25px;
    font-family: "Arimo", Arial, sans-serif;
    font-weight: 700;
    font-size: 20px;
    color: var(--ink-blue);
  }
  .contact-list svg { width: 20px; height: 16px; flex: none; }

  .service-area {
    position: absolute;
    left: 62px;
    top: 281px;
    font-family: "Arimo", Arial, sans-serif;
    font-size: 17.5px;
    color: var(--text-blue);
  }
</style>
</head>
<body>
<div class="canvas">

  <section class="card card--front">
    <div class="card__band"></div>
    <div class="card__rule"></div>
    <h1 class="brand-name">Willow Creek Restoring</h1>
    <ul class="contact-list">
      <li><svg viewBox="0 0 20 16" aria-hidden="true"><path d="M1 5h9V1l9 7-9 7v-4H1z" fill="var(--ink-blue)"/></svg>04 1726 6183</li>
      <li><svg viewBox="0 0 20 16" aria-hidden="true"><path d="M1 5h9V1l9 7-9 7v-4H1z" fill="var(--ink-blue)"/></svg>07 4158 2746</li>
      <li><svg viewBox="0 0 20 16" aria-hidden="true"><path d="M1 5h9V1l9 7-9 7v-4H1z" fill="var(--ink-blue)"/></svg>t.lharte@quillmail.com</li>
    </ul>
    <p class="service-area">Home visits available for cairns and tablelands</p>
  </section>

  <section class="card card--back">
    <div class="card__band"></div>
    <div class="card__rule"></div>
    <p class="tagline">fast safe deep energy healing system tamsin louise<br>harte energy healing / kinesiology and neurotraining</p>
    <h2 class="brand-name">Willow Creek Restoring</h2>
  </section>

</div>
</body>
</html>
```